Gardener needs an A5 leaflet designed modern and trendy

I am a gardener looking to increase business. I am hoping for a leaflet that is informative and eye catching to do this. I would like the flyer to be in keeping with my business card and website. www.bramblevalegardening.co.uk

Target Market(s)

Home owners with money to spend on garden

Industry/Entity Type

Gardener

Colors
000000
acd037

Requirements
Must have
• Pictures to show nice lawns/gardens
• explain what we do as a company. ( see business card for bullet points of what we do)
• 10% off all quoted work with this leaflet ( must be shown when quoting)

```html
<!DOCTYPE html>
<html lang="en">
<head>
<meta charset="utf-8">
<title>Bramblevale Gardening – Leaflet</title>
<link href="https://fonts.googleapis.com/css2?family=Cinzel:wght@700&family=Didact+Gothic&family=Arimo:wght@400;700&display=swap" rel="stylesheet">
<style>
  :root {
    --green: #8cc63f;
    --green-dark: #4f8a2b;
    --heading: #5d8f32;
    --black: #000000;
    --text: #1a1a1a;
    --white: #ffffff;
  }
  * { box-sizing: border-box; margin: 0; padding: 0; }
  html, body { width: 846px; height: 1200px; overflow: hidden; background: var(--white); }
  .leaflet {
    position: relative; width: 846px; height: 1200px; overflow: hidden;
    background: var(--white);
    font-family: "Didact Gothic", "Century Gothic", sans-serif; color: var(--text);
  }
  .hero-photo {
    position: absolute; left: 0; top: 0; width: 846px; height: 460px;
    background:
      radial-gradient(ellipse at 30% 40%, #7a9a4a 0%, transparent 55%),
      radial-gradient(ellipse at 75% 70%, #3f6b2a 0%, transparent 55%),
      radial-gradient(ellipse at 40% 12%, #c67a45 0%, transparent 40%),
      linear-gradient(180deg, #2f4a22 0%, #5b7d3a 45%, #2d4a26 100%);
  }
  .hero-wave { position: absolute; left: 0; top: 300px; width: 846px; height: 180px; }
  .brand-box {
    position: absolute; left: 531px; top: -12px; width: 290px; height: 154px;
    background: var(--black); border: 3px solid var(--white); border-radius: 18px;
    display: flex; align-items: center; justify-content: center; gap: 10px;
    padding-top: 12px;
  }
  .brand-box .brand-dot { width: 14px; height: 14px; border-radius: 50%; background: var(--green); }
  .brand-box .brand-name {
    font-family: "Cinzel", Georgia, serif; font-weight: 700; font-size: 22px;
    color: var(--green); line-height: 1.15; text-align: center; letter-spacing: 1px;
  }
  .offer {
    position: absolute; right: 25px; top: 160px; width: 300px;
    font-family: "Arimo", Arial, sans-serif; font-weight: 700; font-size: 19px; line-height: 24px;
    color: var(--white); text-align: right;
  }
  .section-title {
    position: absolute; left: 34px;
    font-family: "Cinzel", Georgia, serif; font-weight: 700; font-size: 29px;
    color: var(--heading); letter-spacing: 0.5px; line-height: 1;
  }
  .item {
    position: absolute; font-size: 20px; line-height: 25px; padding-left: 17px; white-space: nowrap;
  }
  .item::before {
    content: ""; position: absolute; left: 2px; top: 9px;
    width: 7px; height: 7px; border-radius: 50%; background: var(--green);
  }
  .footer-band { position: absolute; left: 0; top: 1018px; width: 846px; height: 182px; }
  .contact { position: absolute; left: 34px; color: var(--white); font-family: "Arimo", Arial, sans-serif; }
  .contact-name { top: 1052px; font-size: 29px; font-weight: 700; color: var(--green); }
  .contact-role { top: 1086px; font-size: 19px; }
  .contact-phone { top: 1120px; font-size: 24px; font-weight: 700; color: var(--green); }
  .contact-email { top: 1149px; font-size: 20.5px; }
  .contact-web { top: 1173px; font-size: 20.5px; }
  .photo-circle {
    position: absolute; border-radius: 50%; border: 4px solid var(--white);
    box-shadow: 0 0 0 2px #9a9a9a;
  }
  .photo-gardener { left: 425px; top: 1024px; width: 198px; height: 198px;
    background: radial-gradient(circle at 40% 40%, #8aa86a, #4e6e3a 70%); }
  .photo-tulips { left: 628px; top: 1076px; width: 132px; height: 132px;
    background: linear-gradient(180deg, #3d6a2e 0%, #e8c22a 45%, #d9a81c 70%, #3c5e2a 100%); }
  .photo-leaves { left: 696px; top: 1020px; width: 160px; height: 160px;
    background: radial-gradient(circle at 45% 40%, #b9d98a, #6f9c44 75%); }
</style>
</head>
<body>
<main class="leaflet">
  <div class="hero-photo" role="img" aria-label="Photo of a lush landscaped garden with flowering hostas, a lily pond, rocks and a timber fence"></div>
  <svg class="hero-wave" viewBox="0 0 846 180" preserveAspectRatio="none" aria-hidden="true">
    <path d="M0 40 C180 -10 330 90 520 110 C660 125 760 120 846 100 L846 180 L0 180 Z" fill="#7fb83a"/>
    <path d="M0 75 C200 30 340 120 530 135 C670 146 770 140 846 125 L846 180 L0 180 Z" fill="#b8db7c"/>
    <path d="M0 100 C200 70 360 150 540 160 C690 168 780 160 846 150 L846 180 L0 180 Z" fill="#ffffff"/>
  </svg>

  <div class="brand-box">
    <span class="brand-dot"></span>
    <span class="brand-name">Bramblevale<br>Gardening</span>
  </div>
  <p class="offer">10% off all quoted work<br>with this leaflet</p>

  <h2 class="section-title" style="top:466px">Our Commitment</h2>
  <p class="item" style="left:34px;top:497px">All waste removed</p>
  <p class="item" style="left:34px;top:522px">Fully Insured</p>
  <p class="item" style="left:34px;top:547px">Fully qualified greenkeepers</p>
  <p class="item" style="left:451px;top:497px">Reliable, Prompt and Flexible<br>to suit the customer</p>
  <p class="item" style="left:451px;top:547px">Free no obligation quotes</p>

  <h2 class="section-title" style="top:590px">Garden Services</h2>
  <p class="item" style="left:34px;top:621px">Garden Clearances</p>
  <p class="item" style="left:34px;top:646px">Regular maintenance programmes</p>
  <p class="item" style="left:34px;top:671px">Hedge cutting</p>
  <p class="item" style="left:34px;top:697px">Flagging, Paving, Decking and Fencing</p>
  <p class="item" style="left:445px;top:621px">Artificial Grass Installation</p>
  <p class="item" style="left:445px;top:646px">Irrigation system installation</p>
  <p class="item" style="left:445px;top:671px">Landscaping Design</p>

  <h2 class="section-title" style="top:748px">Tree Services</h2>
  <p class="item" style="left:34px;top:779px">Tree pruning</p>
  <p class="item" style="left:218px;top:779px">Tree shaping</p>
  <p class="item" style="left:404px;top:779px">Tree felling</p>
  <p class="item" style="left:571px;top:779px">Tree stump removal</p>

  <h2 class="section-title" style="top:811px">Lawn Services</h2>
  <p class="item" style="left:34px;top:842px">Turfing</p>
  <p class="item" style="left:34px;top:867px">Weed, Pest and<br>Moss control</p>
  <p class="item" style="left:299px;top:842px">Fertiliser applications</p>
  <p class="item" style="left:299px;top:867px">Aeration</p>
  <p class="item" style="left:299px;top:892px">Scarification</p>
  <p class="item" style="left:564px;top:842px">Top Dressing</p>
  <p class="item" style="left:564px;top:867px">Flexible renovation<br>programmes</p>

  <h2 class="section-title" style="top:936px">Sports surface services</h2>
  <p class="item" style="left:34px;top:968px">Verti-Draining</p>
  <p class="item" style="left:34px;top:994px">Hollow Coring</p>
  <p class="item" style="left:299px;top:968px">Top Dressing</p>
  <p class="item" style="left:299px;top:994px">Spraying</p>
  <p class="item" style="left:564px;top:968px">Fertiliser applications</p>

  <svg class="footer-band" viewBox="0 0 846 182" preserveAspectRatio="none" aria-hidden="true">
    <path d="M0 12 C250 -4 600 4 846 40 L846 182 L0 182 Z" fill="#8cc63f"/>
    <path d="M0 20 C250 6 600 14 846 50 L846 182 L0 182 Z" fill="#000000"/>
  </svg>

  <p class="contact contact-name">Owen Hartley</p>
  <p class="contact contact-role">Head Greenkeeper</p>
  <p class="contact contact-phone">07700 900 418</p>
  <p class="contact contact-email">info@bramblevalegardening.co.uk</p>
  <p class="contact contact-web">www.bramblevalegardening.co.uk</p>

  <div class="photo-circle photo-gardener" role="img" aria-label="Photo of a gloved gardener planting flowers in a border"></div>
  <div class="photo-circle photo-leaves" role="img" aria-label="Photo of fresh green tree leaves"></div>
  <div class="photo-circle photo-tulips" role="img" aria-label="Photo of a bed of yellow tulips"></div>
</main>
</body>
</html>
```